KVL cards

Design business cards for renamed business. Korvane Lighting Limited is a leading contract designer of electronic lighting products sepcialising in LED lighting. Need a design that is simple but clear please. Cards for two persons requried.

Target Market(s)

Professional and technical

Industry/Entity Type

Business

Font styles to use
Sans Serif
Other font styles liked:
• tahoma

Colors
ffcf3e

```html
<!DOCTYPE html>
<html lang="en">
<head>
<meta charset="utf-8">
<title>Korvane Lighting Limited – Business Cards</title>
<link rel="stylesheet" href="https://fonts.googleapis.com/css2?family=Tinos:wght@400;700&display=swap">
<style>
  :root {
    --backdrop: #e9e6e0;
    --card-white: #f7f7f7;
    --card-white-shade: #e4e4e4;
    --brand-yellow: #ffcf3e;
    --brand-yellow-deep: #f3c22c;
    --divider-grey: #8a8a8a;
    --ink: #2b2b2b;
    --ink-soft: #555049;
    --icon-dark: #1c1c1c;
  }
  * { box-sizing: border-box; margin: 0; padding: 0; }
  html, body {
    width: 1200px;
    height: 1008px;
    overflow: hidden;
    background: var(--backdrop);
  }
  .sheet {
    width: 1200px;
    height: 1008px;
    display: flex;
    flex-direction: column;
    align-items: center;
    justify-content: center;
    gap: 38px;
  }
  .business-card {
    position: relative;
    width: 780px;
    height: 446px;
    background: linear-gradient(135deg, var(--card-white) 0%, var(--card-white-shade) 100%);
    box-shadow: 0 6px 18px rgba(0,0,0,0.18);
    overflow: hidden;
    font-family: "Tinos", "Times New Roman", serif;
  }
  .card-yellow-panel {
    position: absolute;
    inset: 0;
    background: linear-gradient(160deg, var(--brand-yellow) 0%, var(--brand-yellow-deep) 100%);
    clip-path: polygon(52% 0, 100% 0, 100% 100%, 46% 100%);
  }
  .card-divider {
    position: absolute;
    inset: 0;
    width: 100%;
    height: 100%;
  }
  .company-name {
    position: absolute;
    left: 44px;
    top: 150px;
    width: 320px;
    font-size: 40px;
    line-height: 1.18;
    letter-spacing: 2px;
    text-transform: uppercase;
    color: var(--ink);
  }
  .person {
    position: absolute;
    right: 56px;
    top: 58px;
    text-align: right;
  }
  .person-name {
    font-size: 32px;
    color: var(--ink-soft);
  }
  .person-role {
    font-size: 21px;
    color: var(--ink-soft);
    margin-top: 2px;
  }
  .contact-list {
    position: absolute;
    left: 468px;
    top: 236px;
    list-style: none;
    display: flex;
    flex-direction: column;
    gap: 16px;
  }
  .contact-item {
    display: flex;
    align-items: center;
    gap: 12px;
    font-size: 18px;
    color: var(--ink);
  }
  .contact-icon {
    width: 26px;
    height: 26px;
    flex: none;
  }
</style>
</head>
<body>
<main class="sheet">

  <article class="business-card">
    <div class="card-yellow-panel"></div>
    <svg class="card-divider" viewBox="0 0 780 446" aria-hidden="true">
      <line x1="405.6" y1="0" x2="358.8" y2="446" stroke="var(--divider-grey)" stroke-width="4"/>
    </svg>
    <h1 class="company-name">Korvane Lighting Limited</h1>
    <div class="person">
      <p class="person-name">Your Name</p>
      <p class="person-role">Designation</p>
    </div>
    <ul class="contact-list">
      <li class="contact-item">
        <svg class="contact-icon" viewBox="0 0 26 26" aria-hidden="true">
          <circle cx="13" cy="13" r="13" fill="var(--icon-dark)"/>
          <path d="M9 7.5c.6-.4 1.3-.2 1.6.4l1 1.9c.3.6.1 1.2-.4 1.5l-.7.5c.6 1.6 1.7 2.8 3.3 3.6l.5-.7c.4-.5 1-.6 1.5-.3l1.9 1c.6.3.8 1 .4 1.6l-.8 1.2c-.5.7-1.4 1-2.2.7-3.4-1.2-6-3.9-7.1-7.3-.3-.8 0-1.6.7-2.1z" fill="var(--brand-yellow)"/>
        </svg>
        Phone
      </li>
      <li class="contact-item">
        <svg class="contact-icon" viewBox="0 0 26 26" aria-hidden="true">
          <circle cx="13" cy="13" r="13" fill="var(--icon-dark)"/>
          <rect x="6.5" y="8.5" width="13" height="9" fill="var(--brand-yellow)"/>
          <path d="M6.5 8.5l6.5 5 6.5-5" fill="none" stroke="var(--icon-dark)" stroke-width="1.3"/>
        </svg>
        Mail
      </li>
      <li class="contact-item">
        <svg class="contact-icon" viewBox="0 0 26 26" aria-hidden="true">
          <circle cx="13" cy="13" r="13" fill="var(--icon-dark)"/>
          <g fill="none" stroke="var(--brand-yellow)" stroke-width="1.2">
            <circle cx="13" cy="13" r="7"/>
            <ellipse cx="13" cy="13" rx="3" ry="7"/>
            <line x1="6" y1="13" x2="20" y2="13"/>
            <line x1="7" y1="9.5" x2="19" y2="9.5"/>
            <line x1="7" y1="16.5" x2="19" y2="16.5"/>
          </g>
        </svg>
        Web
      </li>
    </ul>
  </article>

  <article class="business-card">
    <div class="card-yellow-panel"></div>
    <svg class="card-divider" viewBox="0 0 780 446" aria-hidden="true">
      <line x1="405.6" y1="0" x2="358.8" y2="446" stroke="var(--divider-grey)" stroke-width="4"/>
    </svg>
    <h2 class="company-name">Korvane Lighting Limited</h2>
    <div class="person">
      <p class="person-name">Your Name</p>
      <p class="person-role">Designation</p>
    </div>
    <ul class="contact-list">
      <li class="contact-item">
        <svg class="contact-icon" viewBox="0 0 26 26" aria-hidden="true">
          <circle cx="13" cy="13" r="13" fill="var(--icon-dark)"/>
          <path d="M9 7.5c.6-.4 1.3-.2 1.6.4l1 1.9c.3.6.1 1.2-.4 1.5l-.7.5c.6 1.6 1.7 2.8 3.3 3.6l.5-.7c.4-.5 1-.6 1.5-.3l1.9 1c.6.3.8 1 .4 1.6l-.8 1.2c-.5.7-1.4 1-2.2.7-3.4-1.2-6-3.9-7.1-7.3-.3-.8 0-1.6.7-2.1z" fill="var(--brand-yellow)"/>
        </svg>
        Phone
      </li>
      <li class="contact-item">
        <svg class="contact-icon" viewBox="0 0 26 26" aria-hidden="true">
          <circle cx="13" cy="13" r="13" fill="var(--icon-dark)"/>
          <rect x="6.5" y="8.5" width="13" height="9" fill="var(--brand-yellow)"/>
          <path d="M6.5 8.5l6.5 5 6.5-5" fill="none" stroke="var(--icon-dark)" stroke-width="1.3"/>
        </svg>
        Mail
      </li>
      <li class="contact-item">
        <svg class="contact-icon" viewBox="0 0 26 26" aria-hidden="true">
          <circle cx="13" cy="13" r="13" fill="var(--icon-dark)"/>
          <g fill="none" stroke="var(--brand-yellow)" stroke-width="1.2">
            <circle cx="13" cy="13" r="7"/>
            <ellipse cx="13" cy="13" rx="3" ry="7"/>
            <line x1="6" y1="13" x2="20" y2="13"/>
            <line x1="7" y1="9.5" x2="19" y2="9.5"/>
            <line x1="7" y1="16.5" x2="19" y2="16.5"/>
          </g>
        </svg>
        Web
      </li>
    </ul>
  </article>

</main>
</body>
</html>
```